Clinical Hypnotherapist needs business card design

I need a business card design that gives the impression of being approachable yet professional. As a clinical hypnotherapist I need to create trust from my clients to allow me access to their inner mind to enable them to make changes and to start to live the life that they want to live. My website is www.serenvale.com.au and I would like my business cards to reflect my website. I would like a space for appointment details on the back of the card.

```html
<!DOCTYPE html>
<html lang="en">
<head>
<meta charset="utf-8">
<title>Serenvale Hypnotherapy – Business Card</title>
<link rel="stylesheet" href="https://fonts.googleapis.com/css2?family=Noticia+Text:wght@400;700&family=Open+Sans:wght@400;600&display=swap">
<style>
  :root {
    --page-bg: #e4e4e2;
    --panel-green: #e7ecda;
    --accent-purple: #8e2a94;
    --band-grey: #8a8d8c;
    --text-grey: #7b7b78;
    --text-dark: #4a4a48;
    --icon-grey: #8f8f8c;
    --white: #ffffff;
  }
  * { box-sizing: border-box; margin: 0; padding: 0; }
  html, body { width: 1200px; height: 849px; overflow: hidden; }
  body {
    background: var(--page-bg);
    display: flex;
    flex-direction: column;
    align-items: center;
    justify-content: center;
    gap: 44px;
    font-family: "Open Sans", Arial, sans-serif;
  }
  .card {
    position: relative;
    width: 620px;
    height: 352px;
    border-radius: 20px;
    overflow: hidden;
    box-shadow: 0 8px 22px rgba(0,0,0,0.18);
  }
  .card-shapes { position: absolute; inset: 0; width: 100%; height: 100%; }

  /* Back of card */
  .card-back .website {
    position: absolute;
    left: 34px;
    bottom: 26px;
    color: var(--white);
    font-size: 23px;
    letter-spacing: 0.3px;
    text-shadow: 0 1px 3px rgba(0,0,0,0.45);
  }
  .appointments {
    position: absolute;
    left: 494px;
    top: 40px;
    width: 112px;
  }
  .appointments-title {
    font-family: "Noticia Text", Georgia, serif;
    font-size: 13px;
    color: var(--text-dark);
    text-align: center;
  }
  .appointment-field {
    color: var(--accent-purple);
    font-size: 15px;
  }
  .appointment-field .fill-line {
    display: block;
    width: 100%;
    border-bottom: 1.5px dashed var(--accent-purple);
    margin-top: 16px;
  }
  .appointment-field.date { margin-top: 24px; }
  .appointment-field.time { margin-top: 30px; }

  /* Front of card */
  .card-front .identity {
    position: absolute;
    left: 40px;
    top: 34px;
    width: 340px;
  }
  .practitioner-name {
    font-family: "Noticia Text", Georgia, serif;
    font-weight: 400;
    font-size: 27px;
    color: var(--accent-purple);
    line-height: 1.1;
  }
  .practitioner-title {
    font-family: "Noticia Text", Georgia, serif;
    font-weight: 700;
    font-size: 12.5px;
    color: var(--accent-purple);
    margin-top: 2px;
  }
  .practice-location {
    font-size: 15.5px;
    color: var(--text-grey);
    line-height: 1.2;
    margin-top: 20px;
  }
  .phone {
    font-size: 23px;
    color: var(--text-grey);
    margin-top: 16px;
    line-height: 1;
  }
  .card-front .website {
    font-size: 15.5px;
    color: var(--text-grey);
    margin-top: 2px;
  }
  .social-links { display: flex; gap: 8px; margin-top: 12px; }
  .social-dot {
    width: 22px; height: 22px;
    border-radius: 50%;
    background: var(--icon-grey);
  }
</style>
</head>
<body>

  <section class="card card-back" aria-label="Back of business card">
    <svg class="card-shapes" viewBox="0 0 620 352" preserveAspectRatio="none">
      <defs>
        <linearGradient id="seascape" x1="0" y1="0" x2="0.6" y2="1">
          <stop offset="0" stop-color="#9d8cc4"/>
          <stop offset="0.5" stop-color="#d4a596"/>
          <stop offset="1" stop-color="#7a6462"/>
        </linearGradient>
      </defs>
      <rect width="620" height="352" fill="url(#seascape)" role="img" aria-label="Photo of a sunset over the ocean and a calm beach"/>
      <path d="M500,0 C432,100 430,250 482,352 L620,352 L620,0 Z" fill="var(--accent-purple)"/>
      <path d="M512,0 C446,100 444,250 494,352 L620,352 L620,0 Z" fill="var(--band-grey)"/>
      <path d="M516,0 C450,100 448,250 498,352 L620,352 L620,0 Z" fill="var(--panel-green)"/>
    </svg>
    <div class="website">www.serenvale.com.au</div>
    <div class="appointments">
      <div class="appointments-title">Appointments</div>
      <div class="appointment-field date">Date:<span class="fill-line"></span></div>
      <div class="appointment-field time">Time:<span class="fill-line"></span></div>
    </div>
  </section>

  <section class="card card-front" aria-label="Front of business card">
    <svg class="card-shapes" viewBox="0 0 620 352" preserveAspectRatio="none">
      <defs>
        <linearGradient id="portrait" x1="0" y1="0" x2="1" y2="1">
          <stop offset="0" stop-color="#b4bcc2"/>
          <stop offset="0.55" stop-color="#9ea6ad"/>
          <stop offset="1" stop-color="#c98a5a"/>
        </linearGradient>
      </defs>
      <rect width="620" height="352" fill="url(#portrait)" role="img" aria-label="Portrait photo of the hypnotherapist seated against a grey wall"/>
      <path d="M0,0 L390,0 C470,90 470,260 384,352 L0,352 Z" fill="var(--accent-purple)"/>
      <path d="M0,0 L378,0 C456,90 456,260 372,352 L0,352 Z" fill="var(--band-grey)"/>
      <path d="M0,0 L374,0 C452,90 452,260 368,352 L0,352 Z" fill="var(--panel-green)"/>
    </svg>
    <div class="identity">
      <h1 class="practitioner-name">Claire Holloway, CHt</h1>
      <p class="practitioner-title">Clinical Hypnotherapist</p>
      <p class="practice-location">Practice Located Between<br>Brisbane and The Gold Coast</p>
      <p class="phone">0400 315862</p>
      <p class="website">www.serenvale.com.au</p>
      <div class="social-links" aria-label="Social media">
        <span class="social-dot"></span>
        <span class="social-dot"></span>
        <span class="social-dot"></span>
        <span class="social-dot"></span>
      </div>
    </div>
  </section>

</body>
</html>
```